Business Card Design REAL ESTATE SALES PLEASE DESIGN MY CARD 2COLOR CARD WITH RED AS THE DOMINANT

FERNHOLM REALTY
TorLPA Lic# 04738216
RAFAEL " RAFE " MORTON Tel 555 218-3396
TorLPA Lic# 02864057 Fax 555 218-3740
Email: rafe@rafemortonhomes.net Cell 555 902-4481
47530 WREN TERRACE UNION CITY, CA 94312

RAFAEL " RAFE " MORTON
TEL: 555 218-3396 FAX 555 218-3740
Address: 47530 Wren Terrace Union City , CA
EMAIL ADDRESS: rafe@rafemortonhomes.net

```html
<!DOCTYPE html>
<html lang="en">
<head>
<meta charset="utf-8">
<title>Fernholm Realty – Business Card</title>
<link rel="stylesheet" href="https://fonts.googleapis.com/css2?family=Open+Sans:wght@400;600;700&display=swap">
<style>
  :root {
    --brand-red: #c8191e;
    --brand-red-deep: #b8161b;
    --ink: #1f1f1f;
    --slate: #4a4d52;
    --paper: #ffffff;
    --stage: #ecebe8;
  }
  * { box-sizing: border-box; margin: 0; padding: 0; }
  html, body {
    width: 1200px; height: 900px; overflow: hidden;
    background: var(--stage);
    font-family: "Open Sans", Arial, sans-serif;
  }
  .stage {
    position: relative; width: 1200px; height: 900px;
  }
  .card {
    position: absolute; top: 301px;
    width: 520px; height: 297px;
    box-shadow: 0 2px 10px rgba(0,0,0,0.12);
    overflow: hidden;
  }
  /* Front side */
  .card--front { left: 60px; background: var(--brand-red); }
  .front-pattern {
    position: absolute; inset: 0;
    background: linear-gradient(135deg, var(--brand-red) 0%, var(--brand-red-deep) 100%);
  }
  .front-name {
    position: absolute; inset: 0;
    display: flex; align-items: center; justify-content: center;
    color: var(--paper); font-weight: 700; font-size: 34px; letter-spacing: 1px;
  }
  /* Back side */
  .card--back { left: 620px; background: var(--paper); }
  .contact {
    position: absolute; left: 250px; top: 30px;
    font-size: 12.5px; color: var(--ink); line-height: 1;
  }
  .contact-name {
    color: var(--brand-red); font-weight: 700; font-size: 15px;
    margin-bottom: 10px; letter-spacing: 0.3px;
  }
  .contact-row {
    display: flex; align-items: center; gap: 8px; margin-bottom: 6px;
  }
  .contact-row svg { width: 10px; height: 10px; fill: var(--brand-red); flex: none; }
  .licenses { margin-top: 10px; }
  .license { margin-bottom: 4px; font-size: 12.5px; }
  .license-label { color: var(--brand-red); font-weight: 600; }
  .address { margin-top: 12px; font-size: 12.5px; }
  .brand {
    position: absolute; left: 28px; bottom: 38px;
    display: flex; align-items: center; gap: 12px;
  }
  .brand-dot {
    width: 26px; height: 26px; border-radius: 50%; background: var(--brand-red); flex: none;
  }
  .brand-name {
    color: var(--brand-red); font-weight: 700; font-size: 27px; letter-spacing: 0.5px;
  }
</style>
</head>
<body>
<main class="stage">

  <section class="card card--front" aria-label="Card front">
    <div class="front-pattern" role="img" aria-label="Repeating faint brand pattern on red"></div>
    <div class="front-name">FERNHOLM REALTY</div>
  </section>

  <section class="card card--back" aria-label="Card back">
    <div class="contact">
      <p class="contact-name">RAFAEL " RAFE " MORTON</p>
      <p class="contact-row">
        <svg viewBox="0 0 10 10" aria-hidden="true"><path d="M2 0.5 L3.6 2.6 L2.8 3.6 Q4 6 6.4 7.2 L7.4 6.4 L9.5 8 L8.4 9.5 Q3.5 9 0.5 1.6 Z"/></svg>
        <span>555 218-3396</span>
      </p>
      <p class="contact-row">
        <svg viewBox="0 0 10 10" aria-hidden="true"><path d="M2.5 0 H7.5 V10 H2.5 Z M3.5 1 V8 H6.5 V1 Z"/></svg>
        <span>555 902-4481</span>
      </p>
      <p class="contact-row">
        <svg viewBox="0 0 10 10" aria-hidden="true"><path d="M2.5 0 H7 V3 H9.5 V9.5 H0.5 V3 H2.5 Z M3.5 1 V3 H6 V1 Z M2 5 H8 V6 H2 Z M2 7 H8 V8 H2 Z"/></svg>
        <span>555 218-3740</span>
      </p>
      <p class="contact-row">
        <svg viewBox="0 0 10 10" aria-hidden="true"><path d="M0.5 2 H9.5 V8.5 H0.5 Z M1 2.4 L5 5.6 L9 2.4 V3.4 L5 6.6 L1 3.4 Z" fill-rule="evenodd"/></svg>
        <span>rafe@rafemortonhomes.net</span>
      </p>
      <div class="licenses">
        <p class="license"><span class="license-label">TorLPA Lic#</span> 02864057</p>
        <p class="license"><span class="license-label">TorLPA Lic#</span> 04738216</p>
      </div>
      <p class="address">47530 Wren Terrace Union City, CA 94312</p>
    </div>

    <div class="brand">
      <span class="brand-dot" aria-hidden="true"></span>
      <span class="brand-name">FERNHOLM REALTY</span>
    </div>
  </section>

</main>
</body>
</html>
```